European Auto Shop Referral Card 4inches x 6 inches

I would like to have something designed similar to the referral card I have uploaded. The content can be the same, I would like a card designed that matches the colors and font of our Logo.

Front and Back

The particular information is

Q-Tune Motorwerks
42-17 58th Pl
Oak Hollow, NY 11990

(718) 555-0147

www.qtunemotorwerks.example

info@qtunemotorwerks

facebook.com/qtunemotorwerks

instagram name : qtunemotorwerks

yelp : qtunemotorwerks

Industry/Entity Type

Shop

Font styles to use
Sans Serif
Decorative
Script

Colors
33a6d7
85cae6
cee9f5

Requirements
Must have
• My logo, all info pertaining to my shop, all colors and fonts to match the logo theme, widgets to indicate facebook and instagram and yelp.
• PLEASE ALSO INDICATE : European Car Care

```html
<!DOCTYPE html>
<html lang="en">
<head>
<meta charset="utf-8">
<title>Q-Tune Motorwerks – Referral Card</title>
<link rel="stylesheet" href="https://fonts.googleapis.com/css2?family=Michroma&family=Rye&family=Cinzel:wght@400&family=Great+Vibes&family=Roboto:wght@300&display=swap">
<style>
  :root {
    --ink: #2a2a2a;
    --sky: #33a6d7;
    --mist: #85cae6;
    --frost: #cee9f5;
    --teal: #0b7fa6;
    --deep: #13789f;
    --paper: #ffffff;
    --rule: #6a6a6a;
  }
  * { margin: 0; padding: 0; box-sizing: border-box; }
  html, body { width: 686px; height: 1200px; overflow: hidden; background: var(--paper); }
  .card { position: relative; width: 686px; height: 1200px; background: var(--paper); overflow: hidden; }

  .brand { position: absolute; top: 0; left: 0; width: 686px; height: 215px; text-align: center; }
  .brand-name {
    position: absolute; top: 62px; left: 0; width: 100%;
    display: flex; align-items: center; justify-content: center; gap: 14px;
    font-family: "Michroma", sans-serif; font-size: 30px; letter-spacing: 4px; color: var(--ink);
  }
  .brand-mark { width: 26px; height: 26px; background: var(--sky); }
  .brand-tagline {
    position: absolute; top: 136px; left: 0; width: 100%;
    font-family: "Great Vibes", cursive; font-size: 44px; color: var(--sky);
  }

  .band {
    position: absolute; left: 0; width: 686px; background: var(--teal);
    display: flex; align-items: center; justify-content: center;
    font-family: "Michroma", sans-serif; color: var(--paper); letter-spacing: 3px;
  }
  .band-referrals { top: 215px; height: 82px; font-size: 26px; gap: 30px; }
  .band-referrals svg { width: 46px; height: 42px; }
  .band-contact { top: 787px; height: 76px; font-size: 26px; }

  .people {
    position: absolute; top: 297px; left: 0; width: 686px; height: 490px;
    background: radial-gradient(ellipse at 30% 40%, #e4eff6 0%, #d2e3ee 55%, #c8dce9 100%);
  }
  .people span { position: absolute; white-space: nowrap; }
  .word-family { top: 38px; left: 88px; font-family: "Rye", serif; font-size: 84px; color: var(--sky); letter-spacing: 2px; }
  .word-friends { top: 118px; left: 248px; font-family: "Great Vibes", cursive; font-size: 104px; color: var(--deep); }
  .word-neighbors { top: 236px; left: 40px; font-family: "Cinzel", serif; font-size: 100px; color: var(--sky); letter-spacing: 3px; }
  .word-coworkers { top: 356px; left: 200px; font-family: "Great Vibes", cursive; font-size: 88px; color: var(--deep); }

  .contact { position: absolute; top: 863px; left: 0; width: 686px; height: 337px;
    font-family: "Roboto", sans-serif; font-weight: 300; font-size: 21px; color: var(--ink); }
  .contact-divider { position: absolute; left: 343px; top: 26px; width: 1px; height: 288px; background: var(--rule); }
  .contact-address { position: absolute; right: 369px; text-align: right; white-space: nowrap; }
  .contact-social { position: absolute; left: 367px; display: flex; align-items: center; gap: 12px; white-space: nowrap; }
  .social-chip { width: 24px; height: 24px; background: var(--teal); border-radius: 3px; flex: none; }
  .social-chip svg { display: block; }
</style>
</head>
<body>
<main class="card">
  <header class="brand">
    <div class="brand-name"><span class="brand-mark"></span>Q-TUNE MOTORWERKS</div>
    <div class="brand-tagline">European Car Care</div>
  </header>

  <div class="band band-referrals">
    <span>WE</span>
    <svg viewBox="0 0 46 42" aria-label="love">
      <path d="M23 40 C10 30 2 22 2 13 C2 6 7 2 13 2 C18 2 21 5 23 9 C25 5 28 2 33 2 C39 2 44 6 44 13 C44 22 36 30 23 40 Z" fill="#ffffff"/>
    </svg>
    <span>YOUR REFERRALS</span>
  </div>

  <section class="people" role="img" aria-label="Soft pale blue marbled background behind the referral words">
    <span class="word-family">FAMILY</span>
    <span class="word-friends">Friends</span>
    <span class="word-neighbors">NEIGHBORS</span>
    <span class="word-coworkers">Co-Workers</span>
  </section>

  <div class="band band-contact">CONTACT US</div>

  <section class="contact">
    <div class="contact-address" style="top:60px">42-17 58th Pl</div>
    <div class="contact-address" style="top:99px">Oak Hollow, NY 11990</div>
    <div class="contact-address" style="top:177px">(718) 555-0147</div>
    <div class="contact-address" style="top:259px">www.qtunemotorwerks.example</div>

    <div class="contact-divider"></div>

    <div class="contact-social" style="top:59px">
      <span class="social-chip">
        <svg viewBox="0 0 24 24" width="24" height="24" aria-label="email">
          <rect x="4" y="7" width="16" height="11" fill="none" stroke="#fff" stroke-width="1.6"/>
          <path d="M4 7 L12 13 L20 7" fill="none" stroke="#fff" stroke-width="1.6"/>
        </svg>
      </span>info@qtunemotorwerks
    </div>
    <div class="contact-social" style="top:127px"><span class="social-chip"></span>/qtunemotorwerks</div>
    <div class="contact-social" style="top:193px"><span class="social-chip"></span>@qtunemotorwerks</div>
    <div class="contact-social" style="top:259px"><span class="social-chip"></span>qtunemotorwerks</div>
  </section>
</main>
</body>
</html>
```